Cool wedding invitation

I need a creative graphic designer to create and design a hip, funky yet functional wedding invitation.

To give you an idea of what I am looking for I have create a Glimmerboard Board
http://www.glimmerboard-example.com/tanvelo/invitation/

Please provide your best 2 invitations.

Invitation #1 is designed to be printed on plastic. Use both sides
Invitation #2 is designed to be printed on cardboard

Don't be afraid to express your creativity.

Target Market(s)

This is a wedding invitation so the audience is primarily adults aged between 25 to 65.

Industry/Entity Type

Graphic Designer

Requirements
Nice to have
• The attached a colour palette outlines the colours the invitation may use.
• These colours will form the theme of the wedding.

```html
<!DOCTYPE html>
<html lang="en">
<head>
<meta charset="utf-8">
<title>Whitfield &amp; Bellamy Wedding Suite</title>
<link rel="stylesheet" href="https://fonts.googleapis.com/css2?family=Cormorant+Garamond:wght@400;600;700&family=Parisienne&display=swap">
<style>
  :root {
    --backdrop: #4a2c1c;
    --paper: #fbfaf7;
    --wine: #7a1a2c;
    --wine-soft: rgba(122, 26, 44, .55);
    --leaf-dark: #4f3527;
    --leaf-light: #8a6a55;
    --frost: rgba(255, 255, 255, .22);
  }
  * { margin: 0; padding: 0; box-sizing: border-box; }
  html, body { width: 1200px; height: 800px; overflow: hidden; }
  body {
    position: relative;
    background: var(--backdrop);
    font-family: "Cormorant Garamond", Georgia, serif;
    color: var(--wine);
  }
  .card { position: absolute; overflow: hidden; }
  .insert {
    left: 60px; width: 433px; height: 220px;
    background: linear-gradient(90deg, var(--paper) 0 78%, var(--frost) 78% 100%);
  }
  .insert--stay { top: 52px; }
  .insert--route { top: 288px; }
  .insert--reply { top: 525px; }
  .foliage {
    position: absolute;
    background: linear-gradient(90deg, rgba(138,106,85,.5), var(--leaf-dark) 60%, rgba(79,53,39,.3));
    opacity: .85;
  }
  .insert .foliage { left: 288px; top: 0; width: 52px; height: 220px; border-radius: 50% 0 0 50% / 30% 0 0 30%; }
  .script { font-family: "Parisienne", cursive; font-weight: 400; }
  .caps { font-variant: small-caps; }
  .flourish {
    position: absolute; height: 4px; border-radius: 2px;
    background: linear-gradient(90deg, transparent, var(--wine-soft), transparent);
  }
  .insert h2 { position: absolute; left: 18px; top: 20px; font-size: 18px; line-height: 22px; }
  .insert .flourish { left: 36px; top: 46px; width: 60px; }
  .insert-body { position: absolute; left: 18px; top: 66px; width: 268px; font-size: 11px; line-height: 13.5px; }
  .insert-body p { margin-bottom: 11px; }
  .insert--route .insert-body { top: 54px; font-size: 10.5px; line-height: 12.5px; }
  .insert--route .insert-body h3 { font-size: 11.5px; font-weight: 700; line-height: 13px; font-variant: normal; text-transform: uppercase; }
  .insert--route .insert-body p { margin-bottom: 7px; }
  .signoff { text-align: center; font-size: 12px; line-height: 14px; font-variant: normal; }

  .reply-head { position: absolute; left: 0; width: 280px; top: 24px; text-align: center; }
  .reply-head .flourish { position: static; display: block; width: 60px; margin: 0 auto 4px; }
  .reply-head strong { display: block; font-size: 28px; font-weight: 400; line-height: 28px; }
  .reply-head span { display: block; font-size: 12px; line-height: 13px; }
  .reply-line { position: absolute; left: 18px; width: 255px; font-size: 14px; border-bottom: 1px solid var(--wine); line-height: 18px; }
  .options { position: absolute; left: 12px; width: 262px; display: flex; justify-content: space-between; font-size: 10.5px; line-height: 12px; white-space: nowrap; }
  .box { display: inline-block; width: 9px; height: 9px; border: 1px solid var(--wine); margin-right: 6px; vertical-align: -1px; }
  .entree-note { position: absolute; left: 0; width: 290px; top: 156px; text-align: center; font-size: 12px; line-height: 14px; }

  .invitation {
    left: 678px; top: 73px; width: 464px; height: 647px;
    background: var(--paper); text-align: center;
  }
  .invitation .foliage--top { left: 0; top: 0; width: 72px; height: 300px; border-radius: 0 60% 70% 0 / 0 40% 50% 0; }
  .invitation .foliage--bottom { right: 0; top: 400px; width: 70px; height: 247px; border-radius: 70% 0 0 40% / 50% 0 0 30%; }
  .rule { position: absolute; left: 150px; width: 170px; height: 1px; background: var(--wine); }
  .invitation .flourish { left: 170px; width: 130px; }
  .monogram { position: absolute; left: 0; right: 0; top: 62px; font-size: 44px; font-weight: 400; }
  .block { position: absolute; left: 0; right: 0; font-size: 15px; line-height: 20.5px; letter-spacing: .05em; }
  .names { position: absolute; left: 0; right: 0; top: 210px; font-size: 26px; line-height: 25px; }
  .venue { font-weight: 700; font-size: 15px; }
  .reception { position: absolute; left: 0; right: 0; top: 530px; font-size: 21px; }
  .site { position: absolute; left: 0; right: 0; top: 576px; font-size: 14px; letter-spacing: .08em; }
</style>
</head>
<body>
  <section class="card insert insert--stay">
    <div class="foliage" role="img" aria-label="Falling autumn leaves illustration"></div>
    <h2 class="script">Accommodations</h2>
    <div class="flourish" role="img" aria-label="Decorative flourish"></div>
    <div class="insert-body caps">
      <p>For your comfort, a block of rooms have been reserved at:</p>
      <p><strong>Larkspur Grove Resort at Fernhaven</strong><br>1820 Meadowlark Blvd<br>Fernhaven, Florida 34120</p>
      <p>If you would like to make reservations, please call Clara Dunmore and mention the Whitfield/Bellamy wedding for special rates by August 20, 2015</p>
    </div>
  </section>

  <section class="card insert insert--route">
    <div class="foliage" role="img" aria-label="Falling autumn leaves illustration"></div>
    <h2 class="script">Directions</h2>
    <div class="flourish" role="img" aria-label="Decorative flourish"></div>
    <div class="insert-body caps">
      <h3>From Harbor Regional Airport – 25 minutes/32 miles</h3>
      <p>Take South exit to 417 South. Take 417 South and follow the signs to I-4 West. Take I-4 West 3 miles past the Sunfield Park exits to exit 58. Take exit 58 and bear right to the Fernhaven main entrance.</p>
      <h3>Directions from the East – via I-4 West</h3>
      <p>Follow I-4 West. Take exit 58. Bear right off the ramp. Pass through the gates of Fernhaven. At the 2nd stop light, turn right onto Meadowlark Blvd. Hotel is on the left.</p>
      <div class="signoff script">Larkspur Grove Resort at Fernhaven</div>
    </div>
  </section>

  <section class="card insert insert--reply">
    <div class="foliage" role="img" aria-label="Falling autumn leaves illustration"></div>
    <div class="reply-head">
      <i class="flourish" role="img" aria-label="Decorative flourish"></i>
      <strong>RSVP</strong>
      <span>by July 3, 2015</span>
    </div>
    <div class="reply-line script" style="top:84px">M</div>
    <div class="reply-line script" style="top:108px">&amp; M</div>
    <div class="options caps" style="top:135px"><span><i class="box"></i>accepts with pleasure</span><span><i class="box"></i>declines with regrets</span></div>
    <div class="entree-note script">Please indicate entrée selections:</div>
    <div class="options caps" style="top:180px; width:236px; left:24px"><span><i class="box"></i>citrus glazed salmon</span><span><i class="box"></i>chicken marsala</span></div>
  </section>

  <main class="card invitation">
    <div class="foliage foliage--top" role="img" aria-label="Falling autumn leaves illustration"></div>
    <div class="foliage foliage--bottom" role="img" aria-label="Falling autumn leaves illustration"></div>
    <div class="rule" style="top:18px"></div>
    <div class="flourish" style="top:26px" role="img" aria-label="Decorative flourish"></div>
    <h1 class="monogram">E&amp;M</h1>
    <p class="block caps" style="top:134px">Mr. &amp; Mrs. Harold Whitfield<br>request the honor of your presence<br>at the marriage of their daughter</p>
    <p class="names script">Eleanor Whitfield<br>to<br>Marcus Adrian Bellamy</p>
    <p class="block caps" style="top:316px">Saturday, the twenty-second of August<br>two thousand and fifteen<br>six o’clock in the evening</p>
    <div class="flourish" style="top:405px" role="img" aria-label="Decorative flourish"></div>
    <p class="block caps venue" style="top:434px">Larkspur Grove Resort at Fernhaven<br>1820 Meadowlark Blvd<br>Fernhaven, Florida 34120</p>
    <p class="reception script">Reception to follow</p>
    <p class="site caps">eleanorandmarcus.example</p>
    <div class="flourish" style="top:617px" role="img" aria-label="Decorative flourish"></div>
    <div class="rule" style="top:626px"></div>
  </main>
</body>
</html>
```